Ridgeline Thaw Jumpstart Basketball Tournament

This is a flyer to advertise a boys & girls basketball tournament. It will be emailed out to various clubs/organizations in the West in attempt to get them to register for the tournament.
I would like it to have black background with a watermark background of the Salt Lake City city scape. The city scape needs to include the Mountains and downtown buildings of SLC. I would also like a pic of a couple basketball players on the flyer

Colors
85cae6
ffffff

Requirements
Must have
• Black background
• Salt Lake City city scape watermark (showing mountains and downtown buildings)
• Use uploaded info
• Use 1 or 2 uploaded basketball player pics
Nice to have
• Use Carolina blue, black, silver & white for colors

```html
<!DOCTYPE html>
<html lang="en">
<head>
<meta charset="utf-8">
<title>YHA Super Regional National Qualifier – Ridgeline Thaw Jumpstart</title>
<link rel="stylesheet" href="https://fonts.googleapis.com/css2?family=Alfa+Slab+One&family=Oswald:wght@500;600&family=Roboto+Condensed:wght@400;700&display=swap">
<style>
  :root {
    --page: #ffffff;
    --blue-deep: #0a3f7a;
    --blue-mid: #1c6fb8;
    --blue-bright: #2f93d6;
    --carolina: #85cae6;
    --charcoal: #262626;
    --night: #111111;
    --silver: #c9ccd0;
    --silver-light: #eceef0;
    --ink: #111a2a;
    --white: #ffffff;
  }
  * { margin: 0; padding: 0; box-sizing: border-box; }
  html, body { width: 900px; height: 1200px; overflow: hidden; background: var(--page); }
  .canvas { position: relative; width: 900px; height: 1200px; }
  .flyer {
    position: absolute; left: 82px; top: 75px; width: 738px; height: 1045px;
    overflow: hidden; box-shadow: 0 2px 8px rgba(0,0,0,.45);
    background: var(--night);
  }
  .flyer-shapes { position: absolute; inset: 0; }
  .headline {
    position: absolute; left: 0; right: 0; top: 38px; text-align: center;
    font-family: "Alfa Slab One", Georgia, serif; color: var(--white);
    text-shadow: 3px 3px 0 #0b1e38, 0 0 6px rgba(0,0,0,.5);
    line-height: 1;
  }
  .headline .line-one { font-size: 42px; letter-spacing: 1px; }
  .headline .line-two { font-size: 33px; margin-top: 12px; font-variant: small-caps; letter-spacing: 1px; }
  .skyline {
    position: absolute; left: 0; top: 180px; width: 738px; height: 430px;
    background: linear-gradient(180deg, #3a3a3a 0%, #5b5b5b 45%, #2c2c2c 100%);
  }
  .player {
    position: absolute; left: 297px; top: 145px; width: 236px; height: 452px;
    background: radial-gradient(ellipse at 55% 45%, #7fc4e4 0%, #4a9cc6 45%, rgba(60,110,140,.0) 80%);
    border-radius: 40% 40% 10% 10%;
  }
  .event-mark {
    position: absolute; left: 61px; top: 273px; width: 175px; height: 137px;
    background: var(--white); display: flex; align-items: center; justify-content: center;
    text-align: center; padding: 10px;
    font-family: "Oswald", Arial, sans-serif; font-weight: 600; font-size: 20px;
    line-height: 1.1; color: var(--blue-deep); text-transform: uppercase;
  }
  .call-out {
    position: absolute; left: 530px; top: 253px;
    font-family: "Oswald", Arial, sans-serif; font-weight: 500; color: var(--white);
    font-size: 25px; line-height: 1.18; letter-spacing: .3px;
    text-shadow: 1px 1px 3px rgba(0,0,0,.7);
  }
  .venue {
    position: absolute; left: 68px; top: 428px;
    font-family: "Roboto Condensed", Arial, sans-serif; font-weight: 700; color: var(--white);
    font-size: 19px; line-height: 1.32; text-shadow: 1px 1px 3px rgba(0,0,0,.8);
  }
  .event-facts {
    position: absolute; left: 51px; top: 634px;
    font-family: "Roboto Condensed", Arial, sans-serif; font-weight: 700; color: var(--ink);
    font-size: 18px; line-height: 1.3;
  }
  .fine-print {
    position: absolute; left: 392px; top: 637px; width: 320px;
    font-family: "Roboto Condensed", Arial, sans-serif; font-size: 8.6px; line-height: 1.35;
    color: var(--ink); list-style: none;
  }
  .fine-print li { position: relative; padding-left: 7px; }
  .fine-print li::before {
    content: ""; position: absolute; left: 0; top: 4px; width: 3px; height: 3px;
    border-radius: 50%; background: var(--blue-mid);
  }
  .fine-print-rule { position: absolute; left: 378px; top: 632px; width: 1px; height: 100px; background: #555; }
  .price-badge {
    position: absolute; left: 50px; top: 745px; width: 148px; height: 148px; border-radius: 50%;
    background: linear-gradient(180deg, var(--blue-bright), var(--blue-deep));
    border: 4px solid var(--silver); box-shadow: 0 0 0 3px #2a2a2a, 0 3px 8px rgba(0,0,0,.6);
    display: flex; flex-direction: column; align-items: center; justify-content: center;
    font-family: "Oswald", Arial, sans-serif; font-weight: 600; color: var(--white); line-height: .95;
  }
  .price-badge .amount { font-size: 48px; }
  .price-badge .unit { font-size: 34px; color: var(--silver-light); }
  .highlights {
    position: absolute; left: 236px; top: 803px; list-style: none;
    font-family: "Roboto Condensed", Arial, sans-serif; color: var(--white);
    font-size: 19px; line-height: 1.2; text-transform: uppercase;
    text-shadow: 1px 1px 3px rgba(0,0,0,.8);
  }
  .highlights li { position: relative; padding-left: 17px; }
  .highlights li::before {
    content: ""; position: absolute; left: 0; top: 8px; width: 8px; height: 8px;
    border-radius: 50%; background: var(--white);
  }
  .contact-email {
    position: absolute; left: 0; right: 0; bottom: 22px; text-align: center;
    font-family: "Roboto Condensed", Arial, sans-serif; font-size: 13px; letter-spacing: 1.5px;
    color: var(--silver-light);
  }
</style>
</head>
<body>
<div class="canvas">
  <article class="flyer">
    <svg class="flyer-shapes" width="738" height="1045" viewBox="0 0 738 1045" aria-hidden="true">
      <defs>
        <radialGradient id="top-band" cx="50%" cy="30%" r="70%">
          <stop offset="0" stop-color="#2f93d6"/>
          <stop offset="1" stop-color="#0a3f7a"/>
        </radialGradient>
        <linearGradient id="honeycomb" x1="0" y1="0" x2="0" y2="1">
          <stop offset="0" stop-color="#cfd2d5"/>
          <stop offset=".5" stop-color="#f4f5f6"/>
          <stop offset="1" stop-color="#d6d8db"/>
        </linearGradient>
        <linearGradient id="field" x1="0" y1="0" x2="0" y2="1">
          <stop offset="0" stop-color="#2a2a2a"/>
          <stop offset=".5" stop-color="#777"/>
          <stop offset="1" stop-color="#3a3a3a"/>
        </linearGradient>
        <linearGradient id="bottom-band" x1="0" y1="0" x2="0" y2="1">
          <stop offset="0" stop-color="#1c6fb8"/>
          <stop offset="1" stop-color="#0a3f7a"/>
        </linearGradient>
      </defs>
      <rect width="738" height="1045" fill="url(#bottom-band)"/>
      <rect width="738" height="260" fill="url(#top-band)"/>
      <!-- light section and field -->
      <path d="M0 600 Q369 540 738 600 V800 H0 Z" fill="url(#honeycomb)"/>
      <path d="M0 770 Q369 735 738 770 V925 Q369 975 0 925 Z" fill="url(#field)"/>
      <path d="M0 925 Q369 975 738 925" fill="none" stroke="#c9ccd0" stroke-width="5"/>
      <path d="M0 770 Q369 735 738 770" fill="none" stroke="#1c6fb8" stroke-width="4"/>
    </svg>

    <div class="skyline" role="img" aria-label="Greyscale Salt Lake City skyline with mountains and downtown buildings"
         style="clip-path: path('M0 45 Q369 -25 738 45 V410 Q369 460 0 410 Z');"></div>
    <svg class="flyer-shapes" width="738" height="1045" viewBox="0 0 738 1045" aria-hidden="true">
      <path d="M0 225 Q369 155 738 225" fill="none" stroke="#ffffff" stroke-width="6"/>
      <path d="M0 590 Q369 640 738 590" fill="none" stroke="#0b0b0b" stroke-width="5"/>
    </svg>
    <div class="player" role="img" aria-label="Girl in a light blue jersey dribbling a basketball"></div>

    <header class="headline">
      <div class="line-one">YHA SUPER REGIONAL</div>
      <div class="line-two">National Qualifier</div>
    </header>

    <div class="event-mark">Ridgeline Thaw Jumpstart</div>

    <p class="call-out">CALL US TODAY<br>(801) 555-0142</p>

    <p class="venue">ALL UNDER 1 ROOF<br>Summit Court Events Center<br>1820 W. 450 S.<br>Salt Lake City, UT</p>

    <p class="event-facts">DATE: MAY 5-6<br>GRADES:&nbsp; Boys &amp; Girls 2nd – 8th<br>DIVISIONS: Div I &amp; Div II</p>

    <span class="fine-print-rule"></span>
    <ul class="fine-print">
      <li>This event is licensed by the Youth Hoops Association of the U.S., Inc.</li>
      <li>All participants must have a current YHA membership.</li>
      <li>YHA membership may not be included as part of the entry fee to the event.</li>
      <li>YHA membership must be obtained before the competition begins except where the event operator has a laptop available with an internet connection.</li>
      <li>Participants are encouraged to visit the YHA web site www.yhasports.org to obtain their membership.</li>
    </ul>

    <div class="price-badge"><span class="amount">$425</span><span class="unit">TEAM</span></div>

    <ul class="highlights">
      <li>National Qualifyer</li>
      <li>4 Game Guarantee</li>
      <li>West Coast Super Regional Event.</li>
      <li>Already confirmed teams from UT, NV, OR,<br>ID, CO, WY, CA, WA, MT</li>
    </ul>

    <p class="contact-email">coach@ridgelinehoops.com</p>
  </article>
</div>
</body>
</html>
```